Root Crate Filtration Label Design

Need a sticker or label design for our Root Crate to fit an 8x6" area.

UPDATE 9/21/2015:
We eliminated some text and would like to see only the following on the label:

Root Crate Contains:

- Terrestrial Soil
- Lake Sediment
- Organic Matter
- Natural Bacteria
- Minerals & Trace Elements

"STAY RIVER CALM"

We would love to see an illustration of graphic of the outline of our Root Crate (Black plastic box) showing the soil on the inside which is brown and a thin layer of foam on top of the soil inside the box. On top of the box a layer of natural gravel and the plant roots shown growing through the gravel into the soil inside of the box.

Watch this video to get an idea of how the Root Crate fits in an aquarium under a layer of gravel: https://www.clipvaultly.com/watch?t=92&v=qrTm4kLx8Wd
Updates

Target Market(s)

Customers in Retail Stores

Industry/Entity Type

Pet

Font styles to use
Sans Serif

Colors
9bcb3c
0393ce
0255a3
33b8a4
cadf82
add136
86cfc7
cfeae6
eaf2ce

Requirements
Must have
• Stay River Calm and most of the Text - Text can be changed slightly or simplified
Nice to have
• I have attached a picture of a "FRESHWATER Fish Scene" we like.
Should not have
• NOT Too busy - Trying to keep it as simple as possible - Natural Earthy Colors - Realistic Drawings. DO NOT ADD Marine Fish or other MARINE life. This is strictly for FRESHWATER FISH.

```html
<!DOCTYPE html>
<html lang="en">
<head>
<meta charset="utf-8">
<title>Root Crate Filtration Label</title>
<link rel="stylesheet" href="https://fonts.googleapis.com/css2?family=Montserrat:wght@400;600;700;800;900&display=swap">
<style>
  :root {
    --page: #f1f1f1;
    --deep-blue: #0a4fa0;
    --mid-teal: #2f8fa8;
    --leaf-green: #79c07a;
    --lime: #c5dc63;
    --cream: #eef1c9;
    --white: #ffffff;
    --ink: #1c2b3a;
    --accent: #b5d443;
  }
  * { margin: 0; padding: 0; box-sizing: border-box; }
  html, body { width: 784px; height: 1200px; overflow: hidden; background: var(--page); }
  body { font-family: "Montserrat", sans-serif; position: relative; }
  .label { position: absolute; left: 0; width: 784px; }
  .label svg { position: absolute; left: 0; top: 0; }
  .label-front { top: 0; height: 600px; }
  .label-back { top: 590px; height: 570px; }
  .brand-name {
    position: absolute; left: 0; width: 784px; top: 232px;
    text-align: center; font-weight: 900; font-size: 62px; line-height: 1;
    color: var(--lime); white-space: nowrap;
  }
  .product-type {
    position: absolute; left: 0; width: 784px; top: 302px;
    text-align: center; font-weight: 700; font-size: 56px; line-height: 1;
    color: var(--cream); letter-spacing: 5px; white-space: nowrap;
  }
  .contents-title {
    position: absolute; left: 0; width: 784px; top: 106px;
    text-align: center; color: var(--white); font-weight: 700; font-size: 26px; line-height: 1.2;
  }
  .contents-list {
    position: absolute; left: 240px; width: 270px; top: 152px; list-style: none;
  }
  .contents-list li {
    color: var(--white); font-size: 10px; font-weight: 400; white-space: nowrap;
    padding: 3px 0 3px; border-bottom: 1.5px solid var(--white);
  }
  .approach {
    position: absolute; left: 0; width: 784px; top: 256px;
    text-align: center; color: var(--white); font-size: 11px; line-height: 1.5; font-weight: 600;
  }
  .approach .highlight { color: var(--accent); }
  .tagline {
    position: absolute; left: 0; width: 784px; top: 320px;
    text-align: center; font-weight: 900; font-size: 36px; line-height: 1;
    color: var(--ink); letter-spacing: 2px; white-space: nowrap;
  }
  .tagline .tagline-mid { color: var(--accent); }
</style>
</head>
<body>
  <section class="label label-front">
    <svg width="784" height="600" viewBox="0 0 784 600" aria-hidden="true">
      <defs>
        <linearGradient id="flagFill" x1="0" y1="0" x2="0" y2="1">
          <stop offset="0" stop-color="#0a4fa0"/>
          <stop offset="0.55" stop-color="#2f8fa8"/>
          <stop offset="1" stop-color="#79c07a"/>
        </linearGradient>
      </defs>
      <path d="M100 117 C 260 40, 420 150, 684 47 L 684 522 C 500 590, 330 500, 100 590 Z" fill="url(#flagFill)"/>
      <path d="M114 132 C 265 60, 420 168, 668 68 L 668 508 C 500 572, 330 482, 114 574 Z" fill="none" stroke="#ffffff" stroke-width="3"/>
    </svg>
    <div class="brand-name">ROOT-CRATE</div>
    <div class="product-type">FILTRATION</div>
  </section>

  <section class="label label-back">
    <svg width="784" height="570" viewBox="0 0 784 570" aria-hidden="true">
      <defs>
        <linearGradient id="flagFillBack" x1="0" y1="0" x2="0" y2="1">
          <stop offset="0" stop-color="#0a4fa0"/>
          <stop offset="0.55" stop-color="#2f8fa8"/>
          <stop offset="1" stop-color="#79c07a"/>
        </linearGradient>
      </defs>
      <path d="M100 40 C 260 -10, 420 70, 684 8 L 684 506 C 500 575, 330 480, 100 558 Z" fill="url(#flagFillBack)"/>
      <path d="M114 56 C 265 10, 420 88, 668 28 L 668 492 C 500 556, 330 464, 114 542 Z" fill="none" stroke="#ffffff" stroke-width="3"/>
    </svg>
    <h2 class="contents-title">Biological Filter contains</h2>
    <ul class="contents-list">
      <li>Terrestrial Soil</li>
      <li>Lake Sediment</li>
      <li>Organic Matter</li>
      <li>Natural Bacteria, Minerals &amp; Trace Elements</li>
    </ul>
    <p class="approach">
      A Natural Approach for Thriving Fish &amp; Plants in days.<br>
      Plant Roots will settle into soil which stays contained.<br>
      Live Aquatic Plants &amp; Soil are Key to a <span class="highlight">Beautiful</span> Freshwater Aquarium.
    </p>
    <div class="tagline">STAY <span class="tagline-mid">RIVER</span> CALM</div>
  </section>
</body>
</html>
```